Brisk Fixwell business card

I need business card for my business, I think you have all my details.six months ago I design with you car wrap design. We would like to design both side of the card. On front of card we would like logo , Name and our contact details.
At the back we are looking to mentioned our services.
The name will be:
Farzadullah Korimi
Managing Director
Ph:07843529176
Email:info@brisk-fixwell.com
Web:www.brisk-fixwell.com
So we have our logo, you don’t need to change the logo.
Please see the attachment.
Thanks

Target Market(s)

Home improvement

Industry/Entity Type

Home Improvement

Contact Information for Business Card

Company name: Brisk Fixwell
Name: Farzadullah Korimi
Position: Director
Ph:07843529176
Web: www.brisk-fixwell.com
Add: 42 Larkfield Crescent
Hounslow
TW3 9LB
SECOND PERSON
Nasirudin korimi
Position: Handyman
Ph: 07712 634508
Email: info@brisk-fixwell.com
Add: 18 Wrenmoor Park Lane
Hounslow
TW6 2QJ

```html
<!DOCTYPE html>
<html lang="en">
<head>
<meta charset="UTF-8">
<title>Brisk Fixwell – Business Card</title>
<link href="https://fonts.googleapis.com/css2?family=Noto+Sans:wght@400;600;700&display=swap" rel="stylesheet">
<style>
  :root {
    --backdrop: #3b3531;
    --navy: #1f3a8f;
    --red: #d8232f;
    --grey-text: #555a60;
    --rule-grey: #a7a9ac;
    --card-white: #ffffff;
    --grad-start: #21398c;
    --grad-mid: #6a3469;
    --grad-end: #c8283f;
  }
  * { box-sizing: border-box; margin: 0; padding: 0; }
  html, body {
    width: 1200px; height: 1200px; overflow: hidden;
    background: var(--backdrop);
    font-family: "Noto Sans", Arial, sans-serif;
  }
  .canvas { position: relative; width: 1200px; height: 1200px; }

  .card {
    position: absolute;
    width: 720px; height: 411px;
    border-radius: 4px;
    box-shadow: 0 14px 30px rgba(0,0,0,0.35);
    overflow: hidden;
  }

  /* Back of card */
  .card--back {
    left: 70px; top: 110px;
    background: linear-gradient(100deg, var(--grad-start) 0%, var(--grad-mid) 50%, var(--grad-end) 100%);
  }
  .card--back .brand {
    position: absolute; left: 90px; top: 170px;
    display: flex; align-items: center; gap: 20px;
  }
  .brand__name {
    font-weight: 700; font-size: 54px; letter-spacing: 1px;
    text-transform: uppercase; line-height: 1;
  }
  .card--back .brand__name { color: var(--card-white); }
  .brand__mark {
    width: 44px; height: 44px; border-radius: 50%;
  }
  .card--back .brand__mark { border: 5px solid var(--card-white); }

  /* Front of card */
  .card--front {
    left: 410px; top: 660px;
    background: var(--card-white);
  }
  .card--front .brand {
    position: absolute; left: 56px; top: 58px;
    display: flex; align-items: center; gap: 16px;
  }
  .card--front .brand__name { color: var(--navy); font-size: 42px; }
  .card--front .brand__mark { background: var(--red); width: 36px; height: 36px; }
  .brand-rule {
    position: absolute; left: 56px; top: 116px;
    width: 70px; height: 9px; background: var(--rule-grey);
  }

  .person { position: absolute; left: 56px; top: 170px; }
  .person__name {
    color: var(--navy); font-weight: 700; font-size: 25px; letter-spacing: 0.5px;
    text-transform: uppercase;
  }
  .person__role { color: var(--grey-text); font-size: 17px; margin-top: 2px; }

  .contacts {
    position: absolute; left: 56px; top: 262px;
    list-style: none; display: flex; flex-direction: column; gap: 9px;
  }
  .contacts li, .address {
    display: flex; align-items: center; gap: 12px;
    color: #2e3338; font-size: 19px; letter-spacing: 0.3px;
  }
  .icon { width: 20px; height: 20px; flex: none; }

  .divider {
    position: absolute; left: 410px; top: 190px;
    width: 2px; height: 66px; background: var(--red);
  }
  .address {
    position: absolute; left: 440px; top: 180px;
    align-items: flex-start;
  }
  .address .icon { margin-top: 4px; }
  .address__lines { line-height: 1.45; font-size: 17px; }
</style>
</head>
<body>
<main class="canvas">

  <section class="card card--back" aria-label="Card back">
    <div class="brand">
      <span class="brand__name">Brisk Fixwell</span>
      <span class="brand__mark" aria-hidden="true"></span>
    </div>
  </section>

  <section class="card card--front" aria-label="Card front">
    <div class="brand">
      <span class="brand__name">Brisk Fixwell</span>
      <span class="brand__mark" aria-hidden="true"></span>
    </div>
    <div class="brand-rule" aria-hidden="true"></div>

    <div class="person">
      <p class="person__name">Farzadullah Korimi</p>
      <p class="person__role">Director</p>
    </div>

    <ul class="contacts">
      <li>
        <svg class="icon" viewBox="0 0 20 20" aria-hidden="true">
          <circle cx="10" cy="10" r="10" fill="#d8232f"/>
          <path d="M7 5.5l1.8 0 .8 2.2-1.1.9a6 6 0 0 0 2.9 2.9l.9-1.1 2.2.8v1.8c0 .6-.5 1-1.1 1A8 8 0 0 1 6 6.6c0-.6.4-1.1 1-1.1z" fill="#fff"/>
        </svg>
        <span>07843529176</span>
      </li>
      <li>
        <svg class="icon" viewBox="0 0 20 20" aria-hidden="true">
          <circle cx="10" cy="10" r="10" fill="#d8232f"/>
          <g fill="none" stroke="#fff" stroke-width="1.2">
            <circle cx="10" cy="10" r="5"/>
            <ellipse cx="10" cy="10" rx="2.2" ry="5"/>
            <path d="M5 10h10"/>
          </g>
        </svg>
        <span>www.brisk-fixwell.com</span>
      </li>
      <li>
        <svg class="icon" viewBox="0 0 20 20" aria-hidden="true">
          <circle cx="10" cy="10" r="10" fill="#d8232f"/>
          <rect x="5" y="6.5" width="10" height="7" fill="#fff"/>
          <path d="M5 6.5l5 4 5-4" fill="none" stroke="#d8232f" stroke-width="1.1"/>
        </svg>
        <span>info@brisk-fixwell.com</span>
      </li>
    </ul>

    <div class="divider" aria-hidden="true"></div>

    <div class="address">
      <svg class="icon" viewBox="0 0 20 20" aria-hidden="true">
        <circle cx="10" cy="10" r="10" fill="#d8232f"/>
        <path d="M10 4.5a3.8 3.8 0 0 0-3.8 3.8c0 2.8 3.8 7 3.8 7s3.8-4.2 3.8-7A3.8 3.8 0 0 0 10 4.5z" fill="#fff"/>
        <circle cx="10" cy="8.3" r="1.4" fill="#d8232f"/>
      </svg>
      <p class="address__lines">42 Larkfield Crescent<br>Hounslow, TW3 9LB</p>
    </div>
  </section>

</main>
</body>
</html>
```